Wallaby and Rabbit deterrent flyer

I am after a one page flyer for the advertisement of a rabbit and wallaby deterrent. I am doing some targeted advertising of a product that deters rabbits and wallabies from eating plants
Title Possum and Quoll gone
Few pointers i want to hit are:
Guaranteed to prevent animals from eating your plants for up to one month
Rain Fast
All natural
Having trouble with rabbits and wallabies eating your garden look no further
needs to sound like i provide the service of spraying
the product for the customers
Book before August 15 and receive $10 off
Contact Brent at Fern Hollow Yard Crew
04xxxxxxxx
My business card is also attached if it could match it
UPDATE: Change in title to Bandicoot, Possum and Quoll gone

```html
<!DOCTYPE html>
<html lang="en">
<head>
<meta charset="utf-8">
<title>Bandicoot, Possum and Quoll gone – Flyer</title>
<link rel="stylesheet" href="https://fonts.googleapis.com/css2?family=Parisienne&family=Roboto+Condensed:wght@700&family=Roboto:wght@300;400;500&display=swap">
<style>
  :root {
    --green: #5e7c34;
    --green-dark: #4a6628;
    --green-light: #8aa85a;
    --green-pale: #a9c27c;
    --ink: #3d3d3d;
    --grey-text: #5a5a5a;
    --paper: #f4f4f4;
    --white: #ffffff;
    --slate: #4a4a4a;
  }
  * { margin: 0; padding: 0; box-sizing: border-box; }
  html, body { width: 900px; height: 1200px; overflow: hidden; background: var(--paper); }
  .flyer {
    position: relative;
    width: 900px;
    height: 1200px;
    overflow: hidden;
    background: linear-gradient(180deg, #f3f3f3 0%, #e9e9e9 40%, #f0f0f0 100%);
    font-family: "Roboto", Arial, sans-serif;
  }
  .garden-backdrop {
    position: absolute;
    left: 0; top: 560px;
    width: 900px; height: 500px;
    background: radial-gradient(ellipse at 55% 45%, #dfe5d8 0%, #d3dccb 40%, #e6e8e3 75%, rgba(240,240,240,0) 100%);
    opacity: 0.9;
  }
  .hero-shapes { position: absolute; left: 0; top: 0; }
  .mascot-art {
    position: absolute;
    left: 30px; top: 200px;
    width: 180px; height: 260px;
    background: linear-gradient(180deg, #dfe3d8 0%, #e6ddd0 100%);
  }
  .title-band {
    position: absolute;
    left: 0; top: 503px;
    width: 545px; height: 73px;
    background: linear-gradient(180deg, var(--green-light) 0%, var(--green) 55%, var(--green-dark) 100%);
    border-radius: 0 14px 14px 0;
    box-shadow: 0 4px 8px rgba(0,0,0,0.25);
    display: flex; align-items: center;
    padding-left: 20px;
  }
  .title-band h1 {
    font-family: "Parisienne", cursive;
    font-weight: 400;
    font-size: 37px;
    color: var(--white);
    white-space: nowrap;
    text-shadow: 1px 2px 2px rgba(0,0,0,0.35);
  }
  .animal-badge { position: absolute; left: 585px; top: 365px; }
  .headline {
    position: absolute;
    left: 25px; top: 595px;
    font-family: "Roboto Condensed", "Arial Narrow", sans-serif;
    font-weight: 700;
    font-size: 47px;
    line-height: 56px;
    text-shadow: 1px 2px 2px rgba(0,0,0,0.2);
  }
  .headline .lead { color: var(--green); display: block; }
  .headline .mid { color: var(--green); font-family: "Roboto", Arial, sans-serif; font-weight: 400; font-size: 44px; display: block; }
  .headline .tail { color: var(--ink); display: block; }
  .guarantee {
    position: absolute;
    left: 0; top: 776px;
    width: 900px;
    text-align: center;
    font-family: "Roboto", Arial, sans-serif;
    font-weight: 300;
    font-size: 32px;
    line-height: 42px;
    color: var(--grey-text);
    padding-right: 30px;
  }
  .benefits {
    position: absolute;
    left: 0; top: 862px;
    width: 900px;
    text-align: center;
    padding-right: 30px;
    font-family: "Roboto", Arial, sans-serif;
    font-weight: 500;
    font-size: 24px;
    line-height: 30px;
    color: var(--green);
    letter-spacing: 0.5px;
  }
  .offer-band {
    position: absolute;
    left: 88px; top: 906px;
    width: 714px; height: 68px;
    background: linear-gradient(180deg, var(--green-light) 0%, var(--green) 60%, var(--green-dark) 100%);
    border-radius: 4px;
    box-shadow: 0 6px 10px rgba(0,0,0,0.3);
    display: flex; align-items: center; justify-content: center;
    font-family: "Roboto Condensed", "Arial Narrow", sans-serif;
    font-weight: 700;
    font-size: 31px;
    color: var(--white);
    white-space: nowrap;
  }
  .offer-band .amount { font-size: 40px; margin-left: 10px; }
  .footer-shapes { position: absolute; left: 0; top: 930px; }
  .contact {
    position: absolute;
    left: 25px; top: 1030px;
    color: var(--white);
    font-family: "Roboto", Arial, sans-serif;
    font-style: normal;
  }
  .contact .name { font-size: 32px; font-weight: 500; margin-bottom: 8px; }
  .contact p { font-size: 23px; font-weight: 500; line-height: 34px; }
</style>
</head>
<body>
<main class="flyer">
  <div class="garden-backdrop" role="img" aria-label="Soft, faded photograph of a leafy garden path"></div>

  <svg class="hero-shapes" width="900" height="560" viewBox="0 0 900 560">
    <defs>
      <linearGradient id="lawnTone" x1="0" y1="0" x2="0" y2="1">
        <stop offset="0" stop-color="#3c4a2c"/>
        <stop offset="0.45" stop-color="#4f7a35"/>
        <stop offset="1" stop-color="#5f8f3e"/>
      </linearGradient>
    </defs>
    <path d="M193 0 C230 300 380 520 640 545 L900 545 L900 455 Z" fill="#bdbdbd" opacity="0.6"/>
    <path d="M205 0 C245 290 390 505 640 530 L900 520 L900 455 Z" fill="var(--green)"/>
    <path d="M213 0 C255 280 400 490 640 512 L900 500 L900 460 Z" fill="var(--green-pale)"/>
    <path d="M220 0 L900 0 L900 470 L640 495 C410 475 265 275 220 0 Z" fill="url(#lawnTone)" role="img" aria-label="Photograph of two wild rabbits sitting in green grass"/>
  </svg>

  <div class="mascot-art" role="img" aria-label="Illustration of a thumbs-up hand with a green thumb growing a small tree"></div>

  <div class="title-band"><h1>Bandicoot, Possum and Quoll gone</h1></div>

  <svg class="animal-badge" width="310" height="310" viewBox="0 0 310 310">
    <defs>
      <radialGradient id="wallabyTone" cx="0.5" cy="0.45" r="0.6">
        <stop offset="0" stop-color="#8a7a6a"/>
        <stop offset="0.55" stop-color="#5f5a48"/>
        <stop offset="1" stop-color="#3f5a30"/>
      </radialGradient>
    </defs>
    <circle cx="155" cy="155" r="150" fill="var(--white)" stroke="#cfcfcf" stroke-width="2"/>
    <circle cx="155" cy="155" r="138" fill="var(--green)"/>
    <circle cx="155" cy="155" r="132" fill="url(#wallabyTone)" role="img" aria-label="Photograph of a wallaby resting among leaves"/>
  </svg>

  <h2 class="headline">
    <span class="lead">Having trouble with</span>
    <span class="mid">rabbits and wallabies</span>
    <span class="tail">eating your garden?</span>
  </h2>

  <p class="guarantee">Guaranteed to prevent animals from eating<br>your plants for up to one month</p>

  <p class="benefits">Rain Fast &nbsp;•&nbsp; All natural</p>

  <div class="offer-band">Book before August 15 and receive <span class="amount">$10 off</span></div>

  <svg class="footer-shapes" width="900" height="270" viewBox="0 0 900 270">
    <defs>
      <linearGradient id="footGreen" x1="0" y1="0" x2="1" y2="0">
        <stop offset="0" stop-color="var(--green)"/>
        <stop offset="0.6" stop-color="var(--green-light)"/>
        <stop offset="1" stop-color="#c9d8b0"/>
      </linearGradient>
      <linearGradient id="footSlate" x1="0" y1="0" x2="1" y2="0">
        <stop offset="0" stop-color="#7a7a7a"/>
        <stop offset="1" stop-color="var(--slate)"/>
      </linearGradient>
    </defs>
    <polygon points="0,30 900,270 0,270" fill="url(#footGreen)"/>
    <polygon points="0,20 330,110 0,70" fill="#ffffff" opacity="0.5"/>
    <polygon points="583,188 900,70 900,95 640,188" fill="var(--green-pale)"/>
    <polygon points="583,188 900,80 900,270" fill="url(#footSlate)"/>
  </svg>

  <address class="contact">
    <div class="name">Marcuslee</div>
    <p>555.01.23</p>
    <p>marcuslee@fernmail.com</p>
    <p>ABN 98 7654321</p>
  </address>
</main>
</body>
</html>
```